***Rustic Website Design - More design needed after!***

Copperwick Marketing Agency
https://www.instagram.com/tallowfinchco/

Website pages:
Home
About
Design
-Logo Design and Branding
-Graphic Design
Websites
-Hosting, Maintenance and Support
Social Media
Managed Marketing
Portfolio
Contact

I have included a link to our Instagram so you get a feel as to how we want to be.

We want to be approachable to new and rural businesses. - Colours included as image

Target Market(s)

Start Up Businesses & Rural Businesses

Number of Pages Required

2 page

Font styles to use
Serif
Other font styles liked:
• Barnyard, Rustic

Requirements
Must have
• Menu, Social Media Icons, rustic lines like our social media.

```html
<!DOCTYPE html>
<html lang="en">
<head>
<meta charset="utf-8">
<title>Copperwick Marketing</title>
<link rel="stylesheet" href="https://fonts.googleapis.com/css2?family=Montserrat:wght@400;500;600;700&family=Lato:wght@400;700&display=swap">
<style>
:root{
  --cream:#fdf6e6;
  --tan:#e3c9a5;
  --green:#0d4f48;
  --teal:#1c5a52;
  --burgundy:#74203a;
  --yellow:#f8cf2c;
  --ink:#2a2a2a;
  --white:#ffffff;
}
*{box-sizing:border-box;margin:0;padding:0}
html,body{width:1200px;height:4083px;overflow:hidden}
body{position:relative;background:var(--tan);font-family:"Lato",sans-serif;color:var(--ink)}
.abs{position:absolute}
.heading{font-family:"Montserrat",sans-serif;font-weight:700;letter-spacing:1px}

.topbar{left:0;top:0;width:1200px;height:48px;background:var(--cream);font-size:12px;font-family:"Montserrat",sans-serif}
.topbar .item{position:absolute;top:16px;display:flex;align-items:center;gap:8px}
.topbar .social{position:absolute;right:112px;top:17px;display:flex;gap:22px}
.dot{width:12px;height:12px;border-radius:50%;background:var(--ink);display:inline-block}

.nav{left:0;top:48px;width:1200px;height:124px;background:var(--green)}
.brand{position:absolute;left:111px;top:44px;color:var(--white);font-family:"Montserrat",sans-serif;font-weight:700;font-size:24px;line-height:1}
.menu{position:absolute;right:111px;top:52px;display:flex;gap:19px;font-family:"Montserrat",sans-serif;font-weight:600;font-size:15px;color:var(--white)}

.hero{left:0;top:172px;width:1200px;height:573px;background:linear-gradient(110deg,#8c8f92 0%,#5f6b78 40%,#2f4a78 70%,#c47a6a 100%)}
.hero-title{left:108px;top:295px;font-size:41px;color:var(--white)}
.hero-sub{left:113px;top:362px;font-family:"Montserrat",sans-serif;font-size:27px;line-height:38px;color:var(--white)}
.btn{display:flex;align-items:center;justify-content:center;font-family:"Montserrat",sans-serif;font-weight:600;border:2px solid var(--white);color:var(--white)}
.hero-btn{left:117px;top:460px;width:171px;height:51px;font-size:15px;border:3px solid var(--green);background:rgba(255,255,255,.08)}
.hero-wave{left:0;top:600px;width:1200px;height:150px}

.about{left:111px;top:826px;width:976px;height:391px;background:var(--cream)}
.about-photo{left:111px;top:826px;width:491px;height:391px;background:linear-gradient(90deg,#a9826a 0%,#e9e6e2 55%,#f3f1ee 100%)}
.about-frame{left:121px;top:836px;width:956px;height:371px;border:2px solid var(--burgundy)}
.about-title{left:677px;top:880px;font-family:"Montserrat",sans-serif;font-size:30px;font-weight:500;color:var(--ink)}
.about-text{left:677px;top:936px;width:392px;font-size:15px;line-height:25.8px}
.dark-btn{border:2px solid var(--green);color:var(--green);font-size:14px}
.about-btn{left:678px;top:1140px;width:129px;height:39px}

.section-title{width:1200px;text-align:center;font-size:30px;color:var(--ink)}
.card{top:1439px;height:363px;background:var(--yellow)}
.card .photo{position:absolute;left:0;top:0;right:0;height:306px}
.card .label{position:absolute;top:320px;font-family:"Montserrat",sans-serif;font-size:22px}
.card .price{position:absolute;top:320px;font-family:"Montserrat",sans-serif;font-weight:700;font-size:22px;color:var(--green)}
.pager{left:561px;top:1863px;display:flex;gap:9px}
.pager span{width:19px;height:19px;border-radius:50%;background:var(--white)}
.pager span.on{background:var(--green)}

.plan{top:2138px;width:311px;height:178px;text-align:center;color:var(--white)}
.plan .name{position:absolute;top:74px;width:100%;font-family:"Montserrat",sans-serif;font-size:22px;font-weight:500}
.plan .desc{position:absolute;top:114px;width:100%;font-size:15px;line-height:26px}
.badge{top:2056px;width:132px;height:132px;border-radius:50%;background:var(--white);display:flex;align-items:center;justify-content:center}
.badge .core{width:112px;height:112px;border-radius:50%;display:flex;align-items:center;justify-content:center}

.managed{left:0;top:2406px;width:1200px;height:523px;background:linear-gradient(90deg,var(--teal),#215f57 60%,var(--teal))}
.managed-title{left:113px;top:2488px;font-size:30px;color:var(--white)}
.managed-text{left:113px;top:2556px;width:430px;font-family:"Montserrat",sans-serif;font-size:15.5px;line-height:25.8px;color:var(--white)}
.managed-btn{left:113px;top:2821px;width:128px;height:37px;font-size:14px}
.ring{left:637px;top:2457px;width:422px;height:422px;border-radius:50%;background:var(--burgundy);display:flex;align-items:center;justify-content:center}
.ring .inner{width:392px;height:392px;border-radius:50%;background:var(--white);display:flex;align-items:center;justify-content:center}
.ring .photo{width:374px;height:374px;border-radius:50%;background:linear-gradient(135deg,#e9e4dc,#b8a898 60%,#6c5d52)}

.tile{background:linear-gradient(135deg,#d9d3cb,#8e8477)}

.footer-wave{left:0;top:3590px;width:1200px;height:90px}
.footer{left:0;top:3660px;width:1200px;height:423px;background:var(--green);color:var(--white)}
.foot-brand{left:117px;top:3720px;font-family:"Montserrat",sans-serif;font-weight:700;font-size:24px;color:var(--white)}
.foot-text{left:117px;top:3790px;width:230px;font-size:15px;line-height:26px;color:var(--white)}
.foot-social{left:121px;top:3891px;display:flex;gap:22px}
.foot-social .dot{background:var(--white);width:16px;height:16px}
.col-title{font-family:"Montserrat",sans-serif;font-size:22px;font-weight:500;color:var(--white)}
.foot-menu{left:419px;top:3789px;font-size:15px;line-height:26.6px;color:var(--white);list-style:none}
.contact-row{display:flex;gap:14px;align-items:flex-start;font-size:14px;line-height:20px;color:var(--white)}
.email-field{left:848px;top:3796px;width:241px;height:37px;background:var(--white);color:#888;font-size:14px;padding:9px 16px}
.subscribe{left:978px;top:3847px;width:111px;height:38px;font-size:14px;border:2px solid var(--white)}
.rule{left:111px;top:4010px;width:978px;height:1px;background:rgba(255,255,255,.6)}
.copyright{left:0;top:4036px;width:1200px;text-align:center;font-size:12px;color:var(--white);font-family:"Montserrat",sans-serif}
</style>
</head>
<body>

<header>
  <div class="abs topbar">
    <div class="item" style="left:111px">
      <svg width="12" height="16" viewBox="0 0 12 16"><path d="M6 0a6 6 0 0 0-6 6c0 4.5 6 10 6 10s6-5.5 6-10a6 6 0 0 0-6-6zm0 8.5A2.5 2.5 0 1 1 6 3.5a2.5 2.5 0 0 1 0 5z" fill="#2a2a2a"/></svg>
      <span>411 Illum Qui Dolorem</span>
    </div>
    <div class="item" style="left:558px">
      <svg width="14" height="14" viewBox="0 0 24 24"><path d="M6.6 10.8a15.1 15.1 0 0 0 6.6 6.6l2.2-2.2a1 1 0 0 1 1-.25 11.4 11.4 0 0 0 3.6.57 1 1 0 0 1 1 1V20a1 1 0 0 1-1 1A17 17 0 0 1 3 4a1 1 0 0 1 1-1h3.5a1 1 0 0 1 1 1c0 1.25.2 2.45.57 3.57a1 1 0 0 1-.25 1z" fill="#2a2a2a"/></svg>
      <span>+1-123-456-478-00</span>
    </div>
    <div class="social"><span class="dot"></span><span class="dot"></span><span class="dot"></span><span class="dot"></span></div>
  </div>

  <nav class="abs nav">
    <div class="brand">Copperwick<br>Marketing</div>
    <div class="menu">
      <span>HOME</span><span>ABOUT</span><span>DESIGN</span><span>SOCIAL MEDIA</span><span>MANAGED MARKETING</span><span>PORTFOLIO</span><span>CONTACT</span>
    </div>
  </nav>
</header>

<section>
  <div class="abs hero" role="img" aria-label="Photo of hands typing on a laptop showing marketing reports beside a coffee cup"></div>
  <h1 class="abs heading hero-title">COPPERWICK MARKETING</h1>
  <p class="abs hero-sub">LOREM IPSUM DOLOR SIT<br>AMET CONSECTETUR</p>
  <div class="abs btn hero-btn">LEARN MORE</div>
  <svg class="abs hero-wave" viewBox="0 0 1200 150" preserveAspectRatio="none">
    <path d="M0 70 C 120 20, 260 30, 420 70 S 720 150, 900 120 S 1130 70, 1200 30 L1200 150 L0 150 Z" fill="#e3c9a5"/>
    <path d="M0 70 C 120 20, 260 30, 420 70 S 720 150, 900 120 S 1130 70, 1200 30" fill="none" stroke="#f8cf2c" stroke-width="9"/>
  </svg>
</section>

<section>
  <div class="abs about"></div>
  <div class="abs about-photo" role="img" aria-label="Photo of a woman working at a laptop in a bright office"></div>
  <div class="abs about-frame"></div>
  <h2 class="abs about-title">ABOUT US</h2>
  <p class="abs about-text">Lorem Ipsum Dolor Sit Amet, Consectetur Adipiscing Elit, Sed Do Eiusmod Tempor Incididunt Ut Labore Et Dolore Magna Aliqua. Ut Enim Ad Minim Veniam, Quis Nostrud Exercitation Ullamco Laboris Nisi Ut Aliquip Ex Ea Commodo Consequat. Duis Aute Irure Dolor In Reprehenderit In Voluptate Velit Esse Cillum Dolore Eu Fugiat Nulla Pariatur. Excepteur Sint Occaecat Cupidatat</p>
  <div class="abs btn dark-btn about-btn">READ MORE</div>
</section>

<section>
  <h2 class="abs heading section-title" style="top:1354px">SERVICES</h2>
  <div class="abs card" style="left:0;width:112px">
    <div class="photo tile" role="img" aria-label="Photo of a desk with plants and coffee"></div>
    <span class="price" style="left:4px">$65.00</span>
  </div>
  <div class="abs card" style="left:127px;width:466px">
    <div class="photo" style="background:linear-gradient(135deg,#5d6b4a,#8c7a66 50%,#3f3a33)" role="img" aria-label="Photo of a man reviewing logo charts on a laptop"></div>
    <span class="label" style="left:22px">Logo Design</span>
    <span class="price" style="right:66px">$65.00</span>
  </div>
  <div class="abs card" style="left:607px;width:464px">
    <div class="photo" style="background:linear-gradient(120deg,#f2f2f2,#9aa4b0 50%,#1c2330)" role="img" aria-label="Illustration of a hand presenting floating digital screens"></div>
    <span class="label" style="left:22px">Graphic Design</span>
    <span class="price" style="right:34px">$65.00</span>
  </div>
  <div class="abs card" style="left:1086px;width:130px">
    <div class="photo" style="background:linear-gradient(135deg,#c7a58a,#6a4d3a)" role="img" aria-label="Photo of a man in a creative studio"></div>
    <span class="label" style="left:20px">Graphic D</span>
  </div>
  <div class="abs pager"><span></span><span></span><span class="on"></span></div>
</section>

<section>
  <h2 class="abs heading section-title" style="top:1980px">WEBSITES</h2>

  <div class="abs plan" style="left:108px;background:var(--green)">
    <div class="name">HOSTING</div>
    <div class="desc">Ex Ea Commodo Consequat. Duis<br>Aute Irure Dolor In Reprehenderit</div>
  </div>
  <div class="abs badge" style="left:197px"><div class="core" style="background:var(--green)">
    <svg width="60" height="60" viewBox="0 0 60 60" fill="none" stroke="#fff" stroke-width="3"><rect x="8" y="6" width="44" height="12" rx="2"/><rect x="8" y="22" width="44" height="12" rx="2"/><rect x="8" y="38" width="44" height="12" rx="2"/><path d="M14 12h14M14 28h14M14 44h14M30 50v6M12 56h36"/></svg>
  </div></div>

  <div class="abs plan" style="left:442px;background:var(--burgundy)">
    <div class="name">MAINTENANCE</div>
    <div class="desc">Ex Ea Commodo Consequat. Duis<br>Aute Irure Dolor In Reprehenderit</div>
  </div>
  <div class="abs badge" style="left:532px"><div class="core" style="background:var(--burgundy)">
    <svg width="60" height="60" viewBox="0 0 60 60" fill="none" stroke="#fff" stroke-width="3"><rect x="6" y="8" width="48" height="40" rx="2"/><path d="M6 16h48"/><circle cx="22" cy="32" r="7"/><path d="M34 28h14M34 36h14M16 54h28"/></svg>
  </div></div>

  <div class="abs plan" style="left:778px;background:var(--green)">
    <div class="name">SUPPORT</div>
    <div class="desc">Ex Ea Commodo Consequat. Duis<br>Aute Irure Dolor In Reprehenderit</div>
  </div>
  <div class="abs badge" style="left:867px"><div class="core" style="background:var(--green)">
    <svg width="60" height="60" viewBox="0 0 60 60" fill="none" stroke="#fff" stroke-width="3"><circle cx="30" cy="22" r="10"/><path d="M16 22a14 14 0 0 1 28 0M10 54c2-12 10-18 20-18s18 6 20 18z"/></svg>
  </div></div>
</section>

<section>
  <div class="abs managed"></div>
  <h2 class="abs heading managed-title">MANAGED MARKETING</h2>
  <p class="abs managed-text">uisquam Est, Qui Dolorem Ipsum Quia Dolor Sit Amet, Consectetur, Adipisci Velit, Sed Quia Non Numquam Eius Modi Tempora Incidunt Ut Labore Et Dolore Magnam Aliquam Quaerat Voluptatem. Ut Enim Ad Minima Veniam, Quis Nostrum Exercitationem Ullam Corporis Suscipit Laboriosam, Nisi Ut Aliquid Ex Ea Commodi Consequatur? Quis Autem Vel Eum Iure Reprehenderit Qui In Ea Voluptate Velit Esse Quam Nihil Molestiae Consequatur, Vel Illum Qui Dolorem</p>
  <div class="abs btn managed-btn">READ MORE</div>
  <div class="abs ring"><div class="inner"><div class="photo" role="img" aria-label="Photo of a team discussing charts on a whiteboard"></div></div></div>
</section>

<section>
  <h2 class="abs heading section-title" style="top:3036px">PORTFOLIO</h2>
  <div class="abs tile" style="left:111px;top:3108px;width:479px;height:425px;background:linear-gradient(135deg,#d8dde3,#b48a6a 55%,#3c4a5a)" role="img" aria-label="Photo of two colleagues laughing at a computer"></div>
  <div class="abs tile" style="left:598px;top:3108px;width:239px;height:233px;background:linear-gradient(135deg,#3d4a52,#a9a49a)" role="img" aria-label="Photo of a team meeting around a table"></div>
  <div class="abs tile" style="left:598px;top:3352px;width:239px;height:181px;background:linear-gradient(135deg,#e5e2dc,#7c6a5c)" role="img" aria-label="Photo of coworkers gathered around a laptop"></div>
  <div class="abs tile" style="left:846px;top:3108px;width:244px;height:425px;background:linear-gradient(135deg,#cfc9c0,#a06a42 50%,#e8e4de)" role="img" aria-label="Photo of a woman presenting to a colleague"></div>
</section>

<footer>
  <svg class="abs footer-wave" viewBox="0 0 1200 90" preserveAspectRatio="none">
    <path d="M0 55 C 200 10, 420 20, 640 55 S 1000 70, 1200 20 L1200 90 L0 90 Z" fill="#0d4f48"/>
  </svg>
  <div class="abs footer"></div>
  <div class="abs foot-brand">Copperwick<br>Marketing</div>
  <p class="abs foot-text">Lorem ipsum dolor sit amet, consectetur adipiscing elit. nec ullamcorper mattis,</p>
  <div class="abs foot-social"><span class="dot"></span><span class="dot"></span><span class="dot"></span><span class="dot"></span></div>

  <h3 class="abs col-title" style="left:415px;top:3748px">MENU</h3>
  <ul class="abs foot-menu">
    <li>Home</li><li>About</li><li>Design</li><li>Social Media</li><li>Managed</li><li>Marketing</li><li>Portfolio</li>
  </ul>

  <h3 class="abs col-title" style="left:604px;top:3750px">CONTACT US</h3>
  <div class="abs contact-row" style="left:598px;top:3791px">
    <svg width="14" height="18" viewBox="0 0 12 16"><path d="M6 0a6 6 0 0 0-6 6c0 4.5 6 10 6 10s6-5.5 6-10a6 6 0 0 0-6-6zm0 8.5A2.5 2.5 0 1 1 6 3.5a2.5 2.5 0 0 1 0 5z" fill="#fff"/></svg>
    <span>1233Nemo Enim Ipsam<br>Voluptatem Quia</span>
  </div>
  <div class="abs contact-row" style="left:598px;top:3858px">
    <svg width="16" height="16" viewBox="0 0 24 24"><path d="M6.6 10.8a15.1 15.1 0 0 0 6.6 6.6l2.2-2.2a1 1 0 0 1 1-.25 11.4 11.4 0 0 0 3.6.57 1 1 0 0 1 1 1V20a1 1 0 0 1-1 1A17 17 0 0 1 3 4a1 1 0 0 1 1-1h3.5a1 1 0 0 1 1 1c0 1.25.2 2.45.57 3.57a1 1 0 0 1-.25 1z" fill="#fff"/></svg>
    <span>(+000) 123 456 789 0</span>
  </div>
  <div class="abs contact-row" style="left:598px;top:3900px">
    <svg width="20" height="16" viewBox="0 0 20 16" fill="none" stroke="#fff" stroke-width="2"><rect x="1" y="1" width="18" height="14" rx="1"/><path d="M1 2l9 7 9-7"/></svg>
    <span>info@copperwickmarketing.com</span>
  </div>

  <h3 class="abs col-title" style="left:845px;top:3748px">NEWSLETTER</h3>
  <div class="abs email-field">Email</div>
  <div class="abs btn subscribe">Subscribe</div>

  <div class="abs rule"></div>
  <p class="abs copyright">Copyright © 2021 Copperwick Marketing</p>
</footer>

</body>
</html>
```